Pictures required on web page

I would like change three existing pictures on my new website.

The site can be found here:
http://maplebarrelvaults.quillstudio.com.au/

The three pictures to be changed are on the home page:
Purchase- Mixed Packs
Wine Club - Let Us Choose
Education- Wine Courses

I would like somthing stylish, classic and understated that fits in with the theme and feel of the site. I know stylish is a subjective thing. At the moment, the current picture makes the text difficult to read on a destop. Plus I don't think they are a perfect fit for our website anyway. I've attached a photo of our wine course room and also me in the store. Please, don't feel as though you have to use these pictures, but they're there if you want them. However I'm open to completely different photos/graphics to be used.

```html
<!DOCTYPE html>
<html lang="en">
<head>
<meta charset="utf-8">
<title>Maplebarrel – Small winery specialist</title>
<link rel="stylesheet" href="https://fonts.googleapis.com/css2?family=Roboto+Slab:wght@700&family=Roboto:wght@300;400;500&family=Raleway:wght@300;700&display=swap">
<style>
:root{
  --navy:#243559;
  --navy-deep:#1c2a47;
  --nav-bar:#151d2e;
  --white:#ffffff;
  --muted:#c9d2e3;
  --search-bg:#34497a;
  --search-line:#5d76a8;
  --divider:#3a4d77;
  --shipping:#b04a4a;
  --newsletter:#22304f;
  --club-panel:rgba(70,22,40,.88);
  --page:#ffffff;
}
*{box-sizing:border-box;margin:0;padding:0}
html,body{width:1200px;height:639px;overflow:hidden;background:var(--page)}
body{position:relative;font-family:"Roboto",Arial,sans-serif;color:var(--white)}

.site-header{position:absolute;left:0;top:0;width:1200px;height:117px;background:linear-gradient(var(--navy),var(--navy-deep))}
.brand{position:absolute;left:56px;top:22px}
.brand-name{font-family:"Roboto Slab",Georgia,serif;font-weight:700;font-size:42px;line-height:46px}
.brand-tagline{font-family:"Roboto",Arial,sans-serif;font-weight:300;font-size:20px;line-height:24px;margin-top:-2px}

.search{position:absolute;left:366px;top:39px;width:319px;height:37px;background:var(--search-bg);border:1px solid var(--search-line);border-radius:3px}
.search-label{position:absolute;left:14px;top:8px;font-size:16px;color:var(--muted)}
.search svg{position:absolute;right:10px;top:5px}

.utility-nav{position:absolute;top:32px;left:715px;display:flex}
.utility-item{width:88px;height:50px;text-align:center;font-size:12.5px;letter-spacing:.3px;border-left:1px solid var(--divider)}
.utility-item:first-child{border-left:none}
.utility-item svg{display:block;margin:2px auto 6px}

.main-nav{position:absolute;left:0;top:117px;width:1200px;height:53px;background:var(--nav-bar)}
.main-nav ul{list-style:none}
.main-nav li{position:absolute;top:14px;font-size:19.5px;line-height:24px}
.cart{position:absolute;left:980px;top:15px;font-size:14px;display:flex;align-items:center;gap:8px}

.tile{position:absolute;overflow:hidden;display:flex;flex-direction:column;align-items:center;justify-content:center;text-align:center}
.photo{position:absolute;inset:0}
.tile-title{position:relative;font-family:"Raleway",Arial,sans-serif;font-weight:700;font-size:26px;line-height:30px}
.tile-sub{position:relative;font-family:"Raleway",Arial,sans-serif;font-weight:300;font-size:35px;line-height:40px}

.tile-education{left:35px;top:186px;width:361px;height:241px}
.tile-education .photo{background:linear-gradient(120deg,#4a3a2c,#2c241d 55%,#5a4a33)}
.tile-club{left:418px;top:186px;width:363px;height:417px;justify-content:flex-end}
.tile-club .photo{background:linear-gradient(160deg,#c08840,#7a3a2a 45%,#3a2430 80%,#5a5a66)}
.club-panel{position:relative;width:318px;height:110px;margin-bottom:22px;background:var(--club-panel);display:flex;flex-direction:column;justify-content:center;outline:1px solid rgba(255,255,255,.35);outline-offset:-7px}
.tile-packs{left:803px;top:186px;width:361px;height:242px}
.tile-packs .photo{background:linear-gradient(180deg,#6f6a4a,#8a7650 45%,#5b4630 80%,#3d2f22)}

.promo{position:absolute;display:flex;flex-direction:column;align-items:center;justify-content:center;text-align:center}
.promo::after{content:"";position:absolute;inset:22px;border:1px solid rgba(255,255,255,.45)}
.promo-title{font-size:22px;letter-spacing:3px;line-height:28px}
.promo-sub{font-size:15px;letter-spacing:1.4px;line-height:22px}
.promo-shipping{left:35px;top:444px;width:361px;height:162px;background:var(--shipping)}
.promo-newsletter{left:803px;top:441px;width:361px;height:162px;background:var(--newsletter)}
</style>
</head>
<body>
<header class="site-header">
  <div class="brand">
    <div class="brand-name">Maplebarrel</div>
    <div class="brand-tagline">Small winery specialist.</div>
  </div>
  <div class="search">
    <span class="search-label">Search the Cellars</span>
    <svg width="26" height="26" viewBox="0 0 26 26" fill="none" stroke="#fff" stroke-width="2"><circle cx="10.5" cy="10.5" r="7.5"/><path d="M16 16l7 7" stroke-width="3" stroke-linecap="round"/></svg>
  </div>
  <nav class="utility-nav">
    <div class="utility-item"><svg width="20" height="18" viewBox="0 0 20 18" fill="#fff"><path d="M10 1 1 9h3v8h4.5v-5h3v5H16V9h3z"/></svg>HOME</div>
    <div class="utility-item"><svg width="24" height="18" viewBox="0 0 24 18" fill="#fff"><circle cx="12" cy="5" r="3.5"/><circle cx="5" cy="6" r="2.6"/><circle cx="19" cy="6" r="2.6"/><path d="M6 17c0-5 3-7 6-7s6 2 6 7zM0 16c0-4 2-6 5-6 1 0 2 .4 2 .4C5.6 12 5 14 5 16zM24 16c0-4-2-6-5-6-1 0-2 .4-2 .4 1.4 1.6 2 3.6 2 5.6z"/></svg>ABOUT</div>
    <div class="utility-item"><svg width="18" height="18" viewBox="0 0 18 18" fill="none" stroke="#fff" stroke-width="2"><rect x="1.5" y="3" width="15" height="14"/><path d="M1.5 7h15M5 1v4M13 1v4"/></svg>EVENTS</div>
    <div class="utility-item"><svg width="18" height="18" viewBox="0 0 18 18" fill="#fff"><path d="M7.5 0h3l.5 2.5 2 .9 2.2-1.4 2.1 2.1-1.4 2.2.9 2L18 7.5v3l-2.5.5-.9 2 1.4 2.2-2.1 2.1-2.2-1.4-2 .9-.5 2.5h-3L7 15.5l-2-.9-2.2 1.4-2.1-2.1L2.1 11.7l-.9-2L0 10.5v-3l2.5-.5.9-2L2 2.8 4.1.7l2.2 1.4 2-.9zM9 6a3 3 0 100 6 3 3 0 000-6z"/></svg>ACCOUNT</div>
    <div class="utility-item"><svg width="18" height="18" viewBox="0 0 18 18" fill="#fff"><path d="M4 1l3 4-2 2c1 2.5 3.5 5 6 6l2-2 4 3-2 3C8 16 2 10 1 4z"/></svg>CONTACT</div>
  </nav>
</header>

<nav class="main-nav">
  <ul>
    <li style="left:57px">Red Wine</li>
    <li style="left:173px">White Wine</li>
    <li style="left:304px">Sparkling</li>
    <li style="left:418px">Rosé</li>
    <li style="left:495px">Old &amp; Rare</li>
    <li style="left:619px">Stickies</li>
    <li style="left:721px">Imported</li>
    <li style="left:833px">Wine Club</li>
  </ul>
  <div class="cart"><svg width="26" height="22" viewBox="0 0 26 22" fill="#fff"><path d="M0 1h4l1 3h20l-3 9H7.5l.6 2H23v2H6.6L2.6 3H0z"/><circle cx="9" cy="19.5" r="2"/><circle cx="20" cy="19.5" r="2"/></svg>Shopping cart is empty</div>
</nav>

<a class="tile tile-education">
  <div class="photo" role="img" aria-label="Wine barrel, bottle, glass of white wine and green grapes on a wooden table"></div>
  <div class="tile-title">EDUCATION</div>
  <div class="tile-sub">WINE COURSES</div>
</a>

<a class="tile tile-club">
  <div class="photo" role="img" aria-label="Hands raising glasses of red wine in a toast"></div>
  <div class="club-panel">
    <div class="tile-title">WINE CLUB</div>
    <div class="tile-sub">LET US CHOOSE</div>
  </div>
</a>

<a class="tile tile-packs">
  <div class="photo" role="img" aria-label="Wine bottles and glasses on a table overlooking a vineyard at dusk"></div>
  <div class="tile-title">PURCHASE</div>
  <div class="tile-sub">MIXED PACKS</div>
</a>

<div class="promo promo-shipping">
  <div class="promo-title">FREE SHIPPING</div>
  <div class="promo-sub">on orders over $200</div>
</div>

<div class="promo promo-newsletter">
  <div class="promo-title">NEWSLETTER</div>
  <div class="promo-sub">join the newsletter for specials</div>
</div>
</body>
</html>
```